Kit com 6 Layouts de Post para Redes Sociais (Facebook, Instagram e etc) + Capa de Facebookpara RZ SEGUROS E CONSORCIOS
Postado por: gestao.rzseguros_2840395726   Estou Offline

```html
<!DOCTYPE html>
<html lang="pt-BR">
<head>
<meta charset="utf-8">
<title>Post – Seguros</title>
<link href="https://fonts.googleapis.com/css2?family=Montserrat:wght@500;600;700&display=swap" rel="stylesheet">
<style>
  :root {
    --bg-purple: #ad63ba;
    --photo-light: #c58ccf;
    --photo-mid: #9a55a8;
    --photo-dark: #6d3a7e;
    --ink-dark: #3a2452;
    --white: #ffffff;
    --line-light: rgba(255,255,255,0.35);
  }
  html, body {
    margin: 0;
    padding: 0;
    overflow: hidden;
    background: #ffffff;
  }
  .post {
    position: relative;
    width: 1200px;
    height: 1200px;
    background: var(--bg-purple);
    overflow: hidden;
    font-family: "Montserrat", sans-serif;
  }
  .post__art {
    position: absolute;
    inset: 0;
  }
  .headline {
    position: absolute;
    right: 60px;
    top: 350px;
    margin: 0;
    text-align: right;
    font-weight: 700;
    font-size: 68px;
    line-height: 78px;
    letter-spacing: -1px;
  }
  .headline__dark { display: block; color: var(--ink-dark); }
  .headline__light { display: block; color: var(--white); }
  .contact {
    position: absolute;
    left: 80px;
    top: 1012px;
    color: var(--white);
  }
  .contact__label {
    font-size: 15px;
    font-weight: 600;
    margin: 0 0 8px 68px;
    letter-spacing: 0.5px;
  }
  .contact__phone {
    display: flex;
    align-items: center;
    gap: 12px;
    font-size: 24px;
    font-weight: 700;
  }
  .contact__phone small {
    font-size: 16px;
    font-weight: 600;
  }
  .contact__social {
    display: flex;
    align-items: center;
    gap: 10px;
    margin-top: 14px;
    font-size: 15px;
    font-weight: 600;
  }
  .contact__dot {
    width: 16px;
    height: 16px;
    border-radius: 50%;
    background: var(--white);
  }
  .brand {
    position: absolute;
    right: 60px;
    bottom: 78px;
    color: var(--white);
    font-size: 36px;
    font-weight: 500;
  }
</style>
</head>
<body>
<div class="post">
  <svg class="post__art" width="1200" height="1200" viewBox="0 0 1200 1200">
    <defs>
      <linearGradient id="photoTone" x1="0" y1="0" x2="1" y2="1">
        <stop offset="0" stop-color="#b979c4"/>
        <stop offset="0.5" stop-color="#9a55a8"/>
        <stop offset="1" stop-color="#6d3a7e"/>
      </linearGradient>
    </defs>
    <g class="guide-lines" stroke="var(--line-light)" stroke-width="2" fill="none">
      <path d="M430 0 L1100 670"/>
      <path d="M0 520 L520 0"/>
      <path d="M560 1200 L1200 560"/>
    </g>
    <g role="img" aria-label="Foto de duas pessoas trabalhando juntas diante de um notebook">
      <polygon points="380,0 760,290 470,1160 0,1090 0,250 160,0" fill="url(#photoTone)"/>
      <polygon points="470,600 760,890 470,1180 180,890" fill="var(--photo-light)" opacity="0.45"/>
      <polygon points="0,300 200,500 0,700" fill="var(--photo-dark)" opacity="0.5"/>
    </g>
    <polyline class="chevron chevron--dark" points="400,60 300,160 400,260" fill="none" stroke="var(--ink-dark)" stroke-width="50"/>
    <polyline class="chevron chevron--light" points="250,610 110,780 255,935" fill="none" stroke="var(--white)" stroke-width="62"/>
  </svg>

  <h1 class="headline">
    <span class="headline__dark">Seu<br>Texto Aqui</span>
    <span class="headline__light">Seu texto<br>aqui.</span>
  </h1>

  <div class="contact">
    <p class="contact__label">LIGUE AGORA</p>
    <div class="contact__phone">
      <svg width="22" height="22" viewBox="0 0 22 22" aria-hidden="true">
        <circle cx="11" cy="11" r="10" fill="#ffffff"/>
        <path d="M7 7.5c0 4 3.5 7.5 7.5 7.5l1-2-2.2-1-1 1c-1.3-.6-2.3-1.6-2.9-2.9l1-1-1-2.2z" fill="#ad63ba"/>
      </svg>
      <span><small>XX.</small> 0000.0000</span>
    </div>
    <div class="contact__social">
      <span class="contact__dot"></span>
      <span>@SUAEMPRESA</span>
    </div>
  </div>

  <div class="brand">SUA LOGO</div>
</div>
</body>
</html>
```